'Macro at Hand' flyer design.

We need a flyer design for a new company called 'Macro at hand'. We deliver high protein, frozen meals to people in their homes. Mainly aiming at the fitness community. The flyer size will be DL (210mm x 99mm).

We already have a logo as attached below, and would obviously like it to be on the flyer somewhere. We would also like the overall design of the flyer to be in line with the logo (so that the design of the flyer works with the logo and does not contrast it too much).

If you are using any visuals (pictures, background pictures etc.) please do not reference it to any food. Rather we prefer if you used fitness as your inspiration. Please see the picture of Bertil attached for guide. If you are stuck for ideas you can use this photo, however drawn in art. Any pictures you do use please ensure that you have copyright privileges to.

Be as creative as you like with the flyer design. The logo has limited colors however we do not want the flyer to look boring!

These texts will be included on the flyer in the exact order as follows:

- Live a busy lifestyle? No time to meal prep? We do it for you!

- Whether you're bodybuilding or just want truly healthy meals, order from us online.

- Grab and Go meals that you can take to work, school...anywhere.

- High protein, low fat, low sodium.

- No artificial flavours, colours or preservatives.

- Delivered straight to your door, on the day of your choice^.

- Affordable prices.

Remember, if you fail to plan then you plan to fail.

Visit us at www.macroathand.com.au

^Please visit website for conditions.

Target Market(s)

Fitness community.

Industry/Entity Type

Fitness

Requirements
Must have
• Overall design must work with logo.
Nice to have
• Colors.
Should not have
• Any pictures in reference to food.

```html
<!DOCTYPE html>
<html lang="en">
<head>
<meta charset="utf-8">
<title>Macro at Hand – DL Flyer</title>
<link rel="stylesheet" href="https://fonts.googleapis.com/css2?family=Arimo:wght@400;700&family=Roboto+Condensed:wght@400&display=swap">
<style>
  :root {
    --brand-red: #b8182f;
    --arrow-red: #a0162a;
    --ink: #111111;
    --band-red: #e0141c;
    --band-deep: #b0151f;
    --paper: #ffffff;
    --blush: #f3d3d6;
    --rose: #c9525e;
    --figure: #c45a63;
  }
  * { margin: 0; padding: 0; box-sizing: border-box; }
  html, body { width: 1200px; height: 2548px; overflow: hidden; }
  body {
    position: relative;
    font-family: "Arimo", Arial, sans-serif;
    background: linear-gradient(180deg, var(--paper) 0%, #fdf4f5 20%, var(--blush) 42%, var(--rose) 70%, #b8323f 100%);
  }
  .athlete-art {
    position: absolute;
    left: 480px; top: 1120px;
    width: 720px; height: 1428px;
    background: radial-gradient(ellipse at 45% 35%, rgba(196,90,99,0.85) 0%, rgba(196,90,99,0.45) 45%, rgba(196,90,99,0) 75%);
  }
  .brand {
    position: absolute;
    top: 200px; left: 0; width: 1200px;
    display: flex; align-items: center; justify-content: center; gap: 36px;
  }
  .brand-mark { width: 70px; height: 70px; background: var(--brand-red); }
  .brand-name {
    font-weight: 700; font-size: 118px; color: var(--brand-red);
    letter-spacing: 1px; text-transform: uppercase; line-height: 1;
  }
  .features { position: absolute; left: 0; top: 0; width: 1200px; list-style: none; }
  .feature {
    position: absolute; left: 82px; width: 1060px;
    display: flex; align-items: flex-start; gap: 22px;
  }
  .feature svg { flex: 0 0 66px; width: 66px; height: 66px; margin-top: -8px; }
  .feature p {
    font-size: 39px; line-height: 56px; color: var(--ink);
    text-shadow: 1px 1px 2px rgba(255,255,255,0.8);
  }
  .band {
    position: absolute; left: 0; width: 1200px;
    display: flex; flex-direction: column; justify-content: center; align-items: center;
    background: linear-gradient(90deg, var(--band-red) 0%, #d8161e 60%, rgba(216,22,30,0.55) 100%);
    font-family: "Roboto Condensed", "Arial Narrow", sans-serif;
    color: var(--paper); font-size: 61px; line-height: 80px;
    text-shadow: 3px 3px 4px rgba(0,0,0,0.75);
    letter-spacing: -0.5px;
  }
  .band-motto { top: 1860px; height: 226px; }
  .band-conditions {
    top: 2195px; height: 230px;
    background: linear-gradient(90deg, var(--band-red) 0%, var(--band-deep) 70%, rgba(176,21,31,0.6) 100%);
  }
</style>
</head>
<body>
  <div class="athlete-art" role="img" aria-label="Soft silhouette of an athlete drinking from a shaker bottle"></div>

  <header class="brand">
    <span class="brand-mark"></span>
    <span class="brand-name">Macro at Hand</span>
  </header>

  <ul class="features">
    <li class="feature" style="top:623px">
      <svg viewBox="0 0 66 66"><path d="M4 6 L62 33 L4 60 L18 33 Z" fill="var(--arrow-red)"/></svg>
      <p>Live a busy lifestyle? No time to meal prep?<br>we do it for you!</p>
    </li>
    <li class="feature" style="top:808px">
      <svg viewBox="0 0 66 66"><path d="M4 6 L62 33 L4 60 L18 33 Z" fill="var(--arrow-red)"/></svg>
      <p>Whether you’re bodybuilding or just want a<br>truly healthy meals, order from us online.</p>
    </li>
    <li class="feature" style="top:997px">
      <svg viewBox="0 0 66 66"><path d="M4 6 L62 33 L4 60 L18 33 Z" fill="var(--arrow-red)"/></svg>
      <p>Grab and go meals that you can take to work,<br>school....anywhere.</p>
    </li>
    <li class="feature" style="top:1170px">
      <svg viewBox="0 0 66 66"><path d="M4 6 L62 33 L4 60 L18 33 Z" fill="var(--arrow-red)"/></svg>
      <p>High protein, low fat, low sodium.</p>
    </li>
    <li class="feature" style="top:1294px">
      <svg viewBox="0 0 66 66"><path d="M4 6 L62 33 L4 60 L18 33 Z" fill="var(--arrow-red)"/></svg>
      <p>No artificial flavours, colours or preservatives.</p>
    </li>
    <li class="feature" style="top:1423px">
      <svg viewBox="0 0 66 66"><path d="M4 6 L62 33 L4 60 L18 33 Z" fill="var(--arrow-red)"/></svg>
      <p>Delivered straight to your door, on the day of<br>your choice.</p>
    </li>
    <li class="feature" style="top:1610px">
      <svg viewBox="0 0 66 66"><path d="M4 6 L62 33 L4 60 L18 33 Z" fill="var(--arrow-red)"/></svg>
      <p>Affordable prices.</p>
    </li>
  </ul>

  <section class="band band-motto">
    <p>Remember, if you fail to plan then you plan fail.</p>
    <p>Visit us at www.macroathand.com.au</p>
  </section>

  <section class="band band-conditions">
    <p>Please visit us online for conditions.</p>
    <p>Our meals are low in saturated fats</p>
  </section>
</body>
</html>
```